Bright Path Therapies business cards and stationary

Need business cards and stationary designed to match previously made logo for for a new company based in Sydney NSW called 'Bright Path Therapies'.

We provide early intervention services and diagnostic assessment for children with disability and their families. I would like designs that are colourful and child friendly - possibly using feet/footprints/steps on a white background. The final design should communicate that we are family friendly, accepting and fun to work with.

Target Market(s)

Parents and Families
Teachers
Allied Health Professionals

Industry/Entity Type

Psychology

Contact Information for Business Card

Bright Path Therapies
www.brightpaththerapies.example
info@brightpaththerapies.example

Font styles to use
Sans Serif
Decorative
Script

Requirements
Must have
• Match the font and colour scheme of logo, along with footprint picture
Nice to have
• Clean and simple, while reflecting that I am working with families.
• Also- editable for when we make staff specific cards.

```html
<!DOCTYPE html>
<html lang="en">
<head>
<meta charset="utf-8">
<title>Bright Path Therapies – Business Card</title>
<link rel="stylesheet" href="https://fonts.googleapis.com/css2?family=Open+Sans:wght@300;400;600&display=swap">
<style>
  :root {
    --backdrop: #e6e6e6;
    --card: #ffffff;
    --green: #8cc63f;
    --blue: #1679c0;
    --red: #e8403a;
    --title-blue: #1b73b8;
    --teal: #1aa3b3;
    --ink-grey: #6b6b6b;
    --map-grey: #e6e6e6;
  }
  * { box-sizing: border-box; margin: 0; padding: 0; }
  html, body {
    width: 1200px; height: 1000px; overflow: hidden;
    background: var(--backdrop);
    font-family: "Open Sans", sans-serif;
  }
  .canvas { position: relative; width: 1200px; height: 1000px; }

  .card {
    position: absolute; left: 300px;
    width: 600px; height: 380px;
    background: var(--card);
    overflow: hidden;
    box-shadow: 0 6px 18px rgba(0,0,0,.18);
  }
  .card--front { top: 90px; }
  .card--back  { top: 530px; }

  .accent-area {
    position: absolute;
    background: linear-gradient(135deg, rgba(140,198,63,.85) 0%, rgba(22,121,192,.8) 55%, rgba(232,64,58,.8) 100%);
  }
  .card--front .accent-area {
    left: 0; top: 0; width: 190px; height: 380px;
    clip-path: polygon(0 0, 100% 50%, 0 100%);
  }
  .card--back .accent-area--top {
    left: 199px; top: 0; width: 218px; height: 118px;
    clip-path: polygon(0 0, 100% 0, 50% 100%);
  }
  .card--back .accent-area--corner {
    left: 409px; top: 0; width: 191px; height: 266px;
    clip-path: polygon(100% 0, 0 28.6%, 100% 100%);
  }

  .world-map {
    position: absolute;
    background: radial-gradient(closest-side, var(--map-grey) 0%, rgba(230,230,230,.6) 60%, rgba(230,230,230,0) 100%);
  }
  .card--front .world-map { left: 180px; top: 60px; width: 320px; height: 260px; }
  .card--back  .world-map { left: 140px; top: 120px; width: 340px; height: 230px; }

  .brand { position: absolute; display: flex; align-items: center; color: var(--blue); font-weight: 400; }
  .brand__dot { border-radius: 50%; background: var(--red); flex: none; }
  .brand--main { left: 250px; top: 130px; gap: 14px; }
  .brand--main .brand__dot { width: 52px; height: 52px; }
  .brand--main .brand__name { font-size: 32px; line-height: 1.05; letter-spacing: .5px; }
  .brand--main .brand__name span { display: block; font-size: 17px; letter-spacing: 5px; }
  .brand--small { left: 28px; top: 326px; gap: 7px; }
  .brand--small .brand__dot { width: 24px; height: 24px; }
  .brand--small .brand__name { font-size: 13px; }

  .company-title {
    position: absolute; left: 80px; top: 160px;
    font-size: 35px; font-weight: 400; color: var(--title-blue);
    white-space: nowrap;
  }
  .contact { position: absolute; left: 256px; top: 262px; list-style: none; font-size: 13px; }
  .contact__item { display: flex; align-items: center; gap: 8px; height: 25px; }
  .contact__item--email { color: var(--ink-grey); }
  .contact__item--web { color: var(--teal); }
  .contact__icon { width: 12px; height: 12px; flex: none; }
</style>
</head>
<body>
<main class="canvas">

  <section class="card card--front" aria-label="Business card front">
    <div class="accent-area" role="img" aria-label="Colourful decorative arrow graphic in green, blue and red"></div>
    <div class="world-map" role="img" aria-label="Faint grey world map behind the logo"></div>
    <div class="brand brand--main">
      <div class="brand__dot"></div>
      <div class="brand__name">Bright Path<span>THERAPIES</span></div>
    </div>
  </section>

  <section class="card card--back" aria-label="Business card back">
    <div class="accent-area accent-area--top" role="img" aria-label="Colourful decorative arrow graphic in green and red"></div>
    <div class="accent-area accent-area--corner" role="img" aria-label="Colourful decorative arrow graphic in green, red and blue"></div>
    <div class="world-map" role="img" aria-label="Faint grey world map behind the contact details"></div>
    <h1 class="company-title">Bright Path Therapies</h1>
    <ul class="contact">
      <li class="contact__item contact__item--email">
        <svg class="contact__icon" viewBox="0 0 12 12" aria-hidden="true"><rect x="0.5" y="2" width="11" height="8" fill="var(--teal)"/><polyline points="0.5,2 6,6.5 11.5,2" fill="none" stroke="#fff" stroke-width="1"/></svg>
        info@brightpaththerapies.example
      </li>
      <li class="contact__item contact__item--web">
        <svg class="contact__icon" viewBox="0 0 12 12" aria-hidden="true"><circle cx="6" cy="6" r="5.3" fill="none" stroke="var(--ink-grey)" stroke-width="1"/><ellipse cx="6" cy="6" rx="2.3" ry="5.3" fill="none" stroke="var(--ink-grey)" stroke-width="1"/><line x1="0.7" y1="6" x2="11.3" y2="6" stroke="var(--ink-grey)" stroke-width="1"/></svg>
        www.brightpaththerapies.example
      </li>
    </ul>
    <div class="brand brand--small">
      <div class="brand__dot"></div>
      <div class="brand__name">Bright Path Therapies</div>
    </div>
  </section>

</main>
</body>
</html>
```